Bright Path Therapies business cards and stationary

Need business cards and stationary designed to match previously made logo for for a new company based in Sydney NSW called 'Bright Path Therapies'.

We provide early intervention services and diagnostic assessment for children with disability and their families. I would like designs that are colourful and child friendly - possibly using feet/footprints/steps on a white background. The final design should communicate that we are family friendly, accepting and fun to work with.

Target Market(s)

Parents and Families
Teachers
Allied Health Professionals

Industry/Entity Type

Psychology

Contact Information for Business Card

Bright Path Therapies
www.brightpaththerapies.example
info@brightpaththerapies.example

Font styles to use
Sans Serif
Decorative
Script

Requirements
Must have
• Match the font and colour scheme of logo, along with footprint picture
Nice to have
• Clean and simple, while reflecting that I am working with families.
• Also- editable for when we make staff specific cards.

```html
<!DOCTYPE html>
<html lang="en">
<head>
<meta charset="utf-8">
<title>Bright Path Therapies – Business Card</title>
<link rel="stylesheet" href="https://fonts.googleapis.com/css2?family=Open+Sans:wght@400;600;700&display=swap">
<style>
  :root {
    --stage: #d9d9d9;
    --brand-red: #e23b30;
    --brand-red-deep: #c92c23;
    --brand-blue: #1f6fb5;
    --brand-orange: #f29a1d;
    --brand-green: #7cbf3a;
    --ink: #3a3a3a;
    --ink-soft: #666;
    --paper: #ffffff;
    --paper-shade: #f1f1f1;
    --trail-light: #e4e4e4;
  }
  * { box-sizing: border-box; margin: 0; padding: 0; }
  html, body { width: 1200px; height: 904px; overflow: hidden; }
  body {
    background: var(--stage);
    font-family: "Open Sans", Arial, sans-serif;
    position: relative;
  }
  .card {
    position: absolute;
    left: 267px;
    width: 665px;
    height: 380px;
    overflow: hidden;
    box-shadow: 0 4px 14px rgba(0,0,0,.18);
  }
  .card--front {
    top: 50px;
    background: linear-gradient(160deg, var(--brand-red) 0%, var(--brand-red-deep) 100%);
  }
  .card--back {
    top: 474px;
    background: linear-gradient(160deg, var(--paper) 0%, var(--paper-shade) 100%);
  }
  .footprint-trail {
    position: absolute;
    border-radius: 40px;
  }
  .card--front .footprint-trail {
    left: 360px; top: 20px; width: 290px; height: 70px;
    background: linear-gradient(90deg, rgba(190,35,28,0) 0%, rgba(190,35,28,.45) 100%);
  }
  .card--front .footprint-trail--lower {
    left: 20px; top: 270px; width: 260px; height: 80px;
    background: linear-gradient(90deg, rgba(190,35,28,.45) 0%, rgba(190,35,28,0) 100%);
  }
  .card--back .footprint-trail {
    left: 380px; top: 20px; width: 270px; height: 90px;
    background: linear-gradient(90deg, rgba(0,0,0,0) 0%, var(--trail-light) 100%);
  }
  .front-brand {
    position: absolute;
    left: 0; right: 0; top: 150px;
    display: flex; align-items: center; justify-content: center; gap: 16px;
    color: var(--paper);
    font-weight: 700;
    font-size: 34px;
  }
  .brand-dot {
    width: 64px; height: 64px; border-radius: 50%;
    background: var(--paper);
  }
  .back-brand {
    position: absolute;
    left: 40px; top: 104px;
    display: flex; align-items: center; gap: 14px;
    color: var(--brand-blue);
    font-weight: 600;
    font-size: 28px;
  }
  .back-brand .brand-dot { width: 72px; height: 72px; background: var(--brand-red); }
  .staff {
    position: absolute;
    right: 40px; top: 128px;
    text-align: right;
  }
  .staff-name { color: var(--brand-blue); font-weight: 700; font-size: 22px; line-height: 1.1; }
  .staff-role { color: var(--ink-soft); font-size: 15px; }
  .staff-bar { display: flex; margin-top: 6px; width: 150px; height: 5px; margin-left: auto; }
  .staff-bar span { flex: 1; }
  .divider {
    position: absolute;
    left: 40px; right: 190px; top: 220px;
    height: 1.5px; background: var(--ink);
  }
  .address {
    position: absolute;
    left: 40px; top: 250px;
    color: var(--ink); font-size: 16px; line-height: 1.5;
  }
  .contacts {
    position: absolute;
    left: 330px; top: 246px;
    list-style: none;
    color: var(--ink); font-size: 16px; line-height: 1.55;
  }
  .contacts li { display: flex; align-items: center; gap: 10px; }
  .contacts svg { width: 15px; height: 15px; flex: none; }
</style>
</head>
<body>
  <section class="card card--front">
    <div class="footprint-trail" role="img" aria-label="Faint trail of footprints"></div>
    <div class="footprint-trail footprint-trail--lower" role="img" aria-label="Faint trail of footprints"></div>
    <div class="front-brand"><span class="brand-dot"></span>Bright Path Therapies</div>
  </section>

  <section class="card card--back">
    <div class="footprint-trail" role="img" aria-label="Faint grey trail of footprints"></div>
    <div class="back-brand"><span class="brand-dot"></span>Bright Path Therapies</div>
    <div class="staff">
      <div class="staff-name">Jamie Hart</div>
      <div class="staff-role">Manager</div>
      <div class="staff-bar">
        <span style="background:var(--brand-blue)"></span>
        <span style="background:var(--brand-red)"></span>
        <span style="background:var(--brand-orange)"></span>
        <span style="background:var(--brand-green)"></span>
      </div>
    </div>
    <div class="divider"></div>
    <p class="address">12 Harbour Lane, Level 2<br>Sydney NSW 2000</p>
    <ul class="contacts">
      <li>
        <svg viewBox="0 0 16 16"><path d="M4 1l3 3-2 2c1 2 3 4 5 5l2-2 3 3-2 3C7 15 1 9 1 3z" fill="var(--brand-red)"/></svg>
        +61 2 5550 0147
      </li>
      <li>
        <svg viewBox="0 0 16 16"><rect x="1" y="3" width="14" height="10" rx="1" fill="var(--brand-orange)"/><path d="M1 4l7 5 7-5" stroke="#fff" stroke-width="1.4" fill="none"/></svg>
        info@brightpaththerapies.example
      </li>
      <li>
        <svg viewBox="0 0 16 16"><circle cx="8" cy="8" r="7" fill="var(--brand-green)"/><path d="M1 8h14M8 1c-3 4-3 10 0 14M8 1c3 4 3 10 0 14" stroke="#fff" stroke-width="1.1" fill="none"/></svg>
        www.brightpaththerapies.example
      </li>
    </ul>
  </section>
</body>
</html>
```